3 Business Card designs for a company with multiple services

We are a company that has 3 main services:

1) Security - CCTV & Alarm Sepcialists
2) Broadcast - Broadcast Sales and Technical Services
3) Distribution - Quality Products, Quality Service

The broadcast service is for Video Broadcast.

I will include our logos for each service.

I would like to also create a business card design for 7QK in general (see main logo).

Each card will be two-sided. On the front I would think it would include Logo, Name, Posistion and Mobile (and possibly email). And possibly our main number (which may be something like 1800 639 415)

On the back it MUST include a "lined" section to be able to write short quotes / prices.

Then include more details like Phone: 1800 639 415 Fax: 1800 639 412 Postal: PO Box 731, Tallowen, QLD Australia 4290 Website: www.7qk.com.au

We would like a fresh, inovative card design with that "wow check this out" feel about it.

Look forward to seeing what you can do! :)

Corey

Industry/Entity Type

Business

Requirements
Must have
• Quote section on the back!
Editable files.

```html
<!DOCTYPE html>
<html lang="en">
<head>
<meta charset="utf-8">
<title>7QK Broadcast – Business Card Front</title>
<link rel="stylesheet" href="https://fonts.googleapis.com/css2?family=Arimo:wght@400;700&display=swap">
<style>
  :root {
    --card-orange: #cf7f06;
    --card-orange-deep: #c26f04;
    --card-glow: #e8b806;
    --fold-orange: #da8a02;
    --fold-shadow: rgba(120, 60, 0, 0.35);
    --text-light: #fff6dc;
    --text-soft: #fbe7b8;
    --rule-yellow: #ffd23c;
  }
  * { margin: 0; padding: 0; box-sizing: border-box; }
  html, body {
    width: 1200px;
    height: 721px;
    overflow: hidden;
    background: var(--card-orange);
  }
  .card {
    position: relative;
    width: 1200px;
    height: 721px;
    overflow: hidden;
    font-family: "Arimo", Arial, sans-serif;
    background: radial-gradient(ellipse 560px 420px at 560px 330px, var(--card-glow) 0%, #dea005 45%, var(--card-orange) 80%, var(--card-orange-deep) 100%);
  }
  .card__artwork {
    position: absolute;
    left: 0;
    top: 180px;
    width: 900px;
    height: 541px;
    background: radial-gradient(ellipse 380px 240px at 470px 230px, rgba(255, 214, 60, 0.35), rgba(255, 214, 60, 0) 70%);
  }
  .card__folds {
    position: absolute;
    inset: 0;
  }
  .brand {
    position: absolute;
    right: 187px;
    top: 296px;
    display: flex;
    align-items: center;
    gap: 14px;
    color: var(--text-light);
    font-weight: 700;
    font-size: 46px;
    letter-spacing: 2px;
  }
  .brand__mark {
    width: 22px;
    height: 22px;
    background: var(--text-light);
  }
  .contact {
    position: absolute;
    right: 188px;
    top: 462px;
    width: 565px;
    text-align: right;
    color: var(--text-soft);
  }
  .contact__name {
    font-size: 33px;
    font-weight: 400;
    letter-spacing: -0.5px;
    color: #ffffff;
    line-height: 1;
  }
  .contact__rule {
    height: 2px;
    background: var(--rule-yellow);
    margin: 18px 0 9px;
  }
  .contact__line {
    font-size: 23px;
    letter-spacing: 1.2px;
    line-height: 26.5px;
  }
</style>
</head>
<body>
  <main class="card">
    <div class="card__artwork" role="img" aria-label="Soft abstract floral burst in warm yellow tones behind the text"></div>

    <svg class="card__folds" width="1200" height="721" viewBox="0 0 1200 721" aria-hidden="true">
      <defs>
        <filter id="fold-shadow" x="-10%" y="-10%" width="120%" height="130%">
          <feDropShadow dx="0" dy="4" stdDeviation="4" flood-color="#7a3c00" flood-opacity="0.35"/>
        </filter>
      </defs>
      <polygon class="fold fold--left" points="48,16 336,376 743,59 725,0 64,0" fill="#da8a02" filter="url(#fold-shadow)"/>
      <polygon class="fold fold--right" points="725,0 890,216 1172,0" fill="#da8a02" filter="url(#fold-shadow)"/>
    </svg>

    <div class="brand">
      <span class="brand__mark"></span>
      <span class="brand__name">7QK BROADCAST</span>
    </div>

    <section class="contact">
      <h1 class="contact__name">LOREM IPSUM DOLOR</h1>
      <div class="contact__rule"></div>
      <p class="contact__line">Manager</p>
      <p class="contact__line">123.4567.890 ||| 1800 639 415</p>
      <p class="contact__line">LoremIpsumDolor@7qk.com</p>
    </section>
  </main>
</body>
</html>
```